After tattoo calming solution

The label has to be modern, along the same lines as skin care brand “Dew Harbor.” It has to reflect the solutions natural effectiveness and simplicity. The label cannot be over fussy, and must be a little bit clinical, as it really does work. The colours should reflect that the solution calms the skin.

We use a 100ml spray bottle.

Target Market(s)

Anyone with a new tattoo or piercing

Industry/Entity Type

Skincare

Requirements
Must have
• Must reflect its natural calming but still remain a little clinical
Should not have
• It must not look like other flowery tattoo cream solutions.

```html
<!DOCTYPE html>
<html lang="en">
<head>
<meta charset="UTF-8">
<title>Calm Ink &amp; Piercing – Label</title>
<link rel="stylesheet" href="https://fonts.googleapis.com/css2?family=Poppins:wght@600;700&display=swap">
<style>
  :root {
    --backdrop: #e4e0dc;
    --label-white: #ffffff;
    --calm-green: #a9cfa9;
    --ink: #111111;
  }
  html, body {
    margin: 0;
    padding: 0;
    width: 1200px;
    height: 1200px;
    overflow: hidden;
    background: var(--backdrop);
  }
  .canvas {
    position: relative;
    width: 1200px;
    height: 1200px;
  }
  .label {
    position: absolute;
    left: 340px;
    top: 60px;
    width: 520px;
    height: 1080px;
    box-sizing: border-box;
    background: var(--label-white);
    border: 24px solid var(--calm-green);
    box-shadow: 0 10px 40px rgba(0,0,0,0.08);
  }
  .product-name {
    position: absolute;
    left: 50px;
    top: 80px;
    margin: 0;
    font-family: "Poppins", sans-serif;
    font-weight: 700;
    color: var(--ink);
    text-transform: uppercase;
    line-height: 1;
  }
  .product-name .name-main {
    display: block;
    font-size: 64px;
    letter-spacing: 1px;
  }
  .product-name .name-sub {
    display: block;
    margin-top: 12px;
    font-size: 28px;
    letter-spacing: 1.5px;
  }
  .benefit {
    position: absolute;
    left: 50px;
    top: 700px;
    display: flex;
    align-items: flex-end;
    gap: 22px;
  }
  .benefit-bar {
    flex: none;
    width: 70px;
    height: 22px;
    margin-bottom: 2px;
    background: var(--calm-green);
  }
  .benefit-text {
    margin: 0;
    width: 300px;
    font-family: "Poppins", sans-serif;
    font-weight: 600;
    font-size: 20px;
    line-height: 1.2;
    color: var(--calm-green);
  }
  .tagline {
    position: absolute;
    left: 50px;
    top: 810px;
    margin: 0;
    font-family: "Poppins", sans-serif;
    font-weight: 700;
    font-size: 32px;
    line-height: 1.1;
    color: var(--ink);
  }
</style>
</head>
<body>
  <main class="canvas">
    <section class="label">
      <h1 class="product-name">
        <span class="name-main">Calm Ink</span>
        <span class="name-sub">&amp; Piercing</span>
      </h1>
      <div class="benefit">
        <span class="benefit-bar"></span>
        <p class="benefit-text">Reduces inflammation, irritation and encourages natural skin healing</p>
      </div>
      <p class="tagline">Expert skin repair<br>for new tattoos<br>&amp; piercings</p>
    </section>
  </main>
</body>
</html>
```